" Clinica odontologia que ja existia e mudou de dono. Passou por uma reforma e modernizaçao. A clinica tem foco em Ortodontia (aparelhos), seria ótimo se conseguíssemos englobar isto no logo tbm! "

```html
<!DOCTYPE html>
<html lang="pt-BR">
<head>
<meta charset="utf-8">
<title>Lumiara Odontologia Integrada – Pasta</title>
<link href="https://fonts.googleapis.com/css2?family=Montserrat:wght@400;600;700&display=swap" rel="stylesheet">
<style>
  :root {
    --bg: #e9e9e9;
    --brand-blue: #1f7db8;
    --brand-blue-dark: #17649a;
    --paper: #ffffff;
    --line-white: #ffffff;
    --ink-blue: #1c6fa8;
    --ink-grey: #8a8f94;
    --tooth-white: #f2f3f5;
    --tooth-grey: #d9dde1;
    --faint-grey: #eceef0;
    --accent-green: #6cbf3a;
    --accent-pink: #d6297a;
    --accent-purple: #6b3fa0;
    --accent-orange: #f28c28;
  }
  * { box-sizing: border-box; margin: 0; padding: 0; }
  html, body { width: 1200px; height: 1200px; overflow: hidden; }
  body {
    background: var(--bg);
    font-family: "Montserrat", sans-serif;
    position: relative;
  }

  .panel { position: absolute; }
  .panel--back {
    left: 120px; top: 204px;
    width: 492px; height: 744px;
    background: var(--brand-blue);
  }
  .panel--front {
    left: 612px; top: 204px;
    width: 456px; height: 708px;
    background: var(--paper);
  }

  .decoration {
    position: absolute;
    left: 612px; top: 212px;
    width: 204px; height: 580px;
    border-radius: 0 90px 40px 0;
    background: linear-gradient(180deg, var(--faint-grey) 0%, #f5f6f7 100%);
  }

  .artwork {
    position: absolute;
    left: 282px; top: 250px;
    width: 336px; height: 540px;
    border-radius: 110px 60px 40px 70px;
    background: linear-gradient(100deg,
      var(--tooth-white) 0%, var(--tooth-grey) 55%, var(--tooth-white) 68%,
      var(--accent-green) 78%, var(--accent-purple) 86%,
      var(--accent-pink) 93%, var(--accent-orange) 100%);
  }

  .fold-hole {
    position: absolute;
    width: 30px; height: 30px;
    border: 2px solid #555a5f;
    border-radius: 50%;
    background: var(--paper);
    clip-path: inset(0 0 0 50%);
    left: 597px;
  }
  .fold-hole--top { top: 321px; }
  .fold-hole--bottom { top: 685px; }

  .contact {
    position: absolute;
    left: 140px; top: 752px;
    color: var(--line-white);
    font-size: 8px; line-height: 11px;
  }
  .contact__brand {
    display: flex; align-items: center; gap: 5px;
    font-size: 11px; font-weight: 700; letter-spacing: 1px;
    margin-bottom: 5px;
  }
  .contact__mark { width: 9px; height: 9px; background: var(--line-white); }

  .rule {
    position: absolute;
    left: 240px; top: 820px;
    width: 360px; height: 3px;
    background: var(--line-white);
  }

  .pocket {
    position: absolute;
    left: 108px; top: 840px;
    width: 216px; height: 108px;
    background: var(--brand-blue);
    border-top: 2px solid var(--brand-blue-dark);
    border-left: 2px solid var(--brand-blue-dark);
  }
  .pocket__card-slot {
    position: absolute;
    left: 36px; top: 22px;
    width: 156px; height: 62px;
    border: 2px solid var(--line-white);
    border-radius: 4px;
  }

  .brand {
    position: absolute;
    left: 860px; top: 756px;
    width: 204px;
    text-align: center;
  }
  .brand__name {
    display: flex; align-items: center; justify-content: center; gap: 8px;
    font-size: 32px; font-weight: 600; color: var(--ink-blue);
    letter-spacing: 0.5px; line-height: 1;
  }
  .brand__mark { width: 14px; height: 14px; background: var(--ink-blue); }
  .brand__tagline {
    margin-top: 4px;
    font-size: 8px; font-weight: 600; color: var(--ink-grey);
    letter-spacing: 2px;
  }
</style>
</head>
<body>
  <section class="panel panel--back"></section>
  <section class="panel panel--front"></section>

  <div class="decoration" role="img" aria-label="Faint grey mosaic tooth shape running along the fold"></div>
  <div class="artwork" role="img" aria-label="Illustration of a large white tooth wearing an orthodontic bracket, with green, purple, pink and orange mosaic pieces behind it"></div>

  <span class="fold-hole fold-hole--top"></span>
  <span class="fold-hole fold-hole--bottom"></span>

  <div class="contact">
    <div class="contact__brand"><span class="contact__mark"></span>LUMIARA</div>
    <p>Rua Aurora, 480, Centro</p>
    <p>São Paulo, SP</p>
    <p>T (11) 4000-1020</p>
    <p>F (11) 4000-1021</p>
    <p>contato@lumiara.com.br</p>
    <p>www.lumiara.com.br</p>
  </div>
  <div class="rule"></div>
  <div class="pocket"><div class="pocket__card-slot"></div></div>

  <div class="brand">
    <div class="brand__name"><span class="brand__mark"></span>LUMIARA</div>
    <div class="brand__tagline">ODONTOLOGIA INTEGRADA</div>
  </div>
</body>
</html>
```